KRTLO Promotion Flyer to raise money and communicate our goals

We need a flyer that promotes our organization. We are a 501(c)3 trying to raise money for Arts, Education and Entrepreneurship in our small town.

We promote a social events that improve qualtiy of life and educate people on how to start and expand businesses. Our goal is to make downtown an active and thriving place with many things for people to do and enjoy as well as create a favorable place for business.

Target Market(s)

Wealthy donors and Organizations with cash

Industry/Entity Type

Education

Colors

Designer to choose colors to be used in the design.

Requirements
Must have
• Eye catching graphics and look very professional
• Should appeal to men and women
Nice to have
• Make use of any known psychological colors and fonts etc... that appeal to philanthropic people
Should not have
• Should not be complicated or confusing

```html
<!DOCTYPE html>
<html lang="en">
<head>
<meta charset="utf-8">
<title>KRTLO Promotion Flyer</title>
<link rel="stylesheet" href="https://fonts.googleapis.com/css2?family=Open+Sans:wght@400;600;700&family=Roboto+Condensed:wght@700&display=swap">
<style>
:root{
  --bg:#ece9e4;
  --navy:#0d2a4a;
  --blue:#1a93cf;
  --green:#7ab929;
  --green-band:#72b53a;
  --white:#ffffff;
  --ink:#1d2230;
  --intro-bg:#f1f2f4;
}
*{margin:0;padding:0;box-sizing:border-box}
html,body{width:1200px;height:1199px;overflow:hidden;background:var(--bg)}
body{position:relative;font-family:"Open Sans",Arial,sans-serif}
.flyer{position:absolute;left:228px;top:74px;width:743px;height:1050px;background:var(--white);box-shadow:0 6px 18px rgba(0,0,0,.25);overflow:hidden}
.hero-photo{position:absolute;left:0;top:0;width:743px;height:348px;
  background:linear-gradient(180deg,#e6eaee 0%,#d9dfe4 45%,#a9a496 58%,#6f8a4c 68%,#5d823a 100%)}
.title-band{position:absolute;left:0;top:348px;width:743px;height:102px;background:var(--navy)}
.title-band h1{position:absolute;left:35px;top:24px;font-family:"Roboto Condensed",Arial,sans-serif;font-weight:700;font-size:25px;color:var(--green);letter-spacing:.2px}
.title-band p{position:absolute;left:35px;top:57px;font-family:"Roboto Condensed",Arial,sans-serif;font-weight:700;font-size:17.5px;color:var(--white)}
.brand-box{position:absolute;left:576px;top:0;width:130px;height:102px;background:var(--white);display:flex;align-items:center;justify-content:center;gap:7px}
.brand-box .mark{width:14px;height:14px;background:var(--blue)}
.brand-box .name{font-family:"Open Sans",Arial,sans-serif;font-weight:700;font-size:20px;color:var(--navy)}
.accent-rule{position:absolute;left:0;top:450px;width:743px;height:10px;background:var(--blue)}
.intro{position:absolute;left:0;top:460px;width:743px;height:138px;background:var(--intro-bg);padding:25px 30px 0;text-align:center;font-size:14.3px;line-height:18px;color:var(--ink)}
.goals{position:absolute;left:0;top:598px;width:743px;height:250px;background:var(--navy)}
.goal-tab{position:absolute;left:133px;top:580px;width:477px;height:38px;background:var(--blue);color:var(--white);font-weight:700;font-size:17px;text-align:center;line-height:38px;z-index:2}
.goal-tab::after{content:"";position:absolute;left:230px;top:38px;border-left:16px solid transparent;border-right:16px solid transparent;border-top:16px solid var(--blue)}
.goal{position:absolute;display:flex;gap:13px;color:var(--white);font-size:14.3px;line-height:18px}
.goal svg{flex:none;margin-top:1px}
.goal b{font-weight:700}
.goal.small{font-size:13.3px;line-height:16.5px}
.appeal{position:absolute;left:0;top:848px;width:743px;height:202px;background:var(--green-band);padding:20px 38px 0;text-align:center;font-size:14.3px;line-height:18px;color:var(--ink)}
.appeal strong{display:block;margin-top:6px;font-weight:700}
</style>
</head>
<body>
<main class="flyer">
  <div class="hero-photo" role="img" aria-label="Town park with flag poles, a large hall, a white gazebo, trees and a winding path"></div>

  <header class="title-band">
    <h1>THE KERTLOW SMALL BUSINESS ASSOCIATION</h1>
    <p>Local leader in the areas of Arts, Education and Entrepreneurship</p>
    <div class="brand-box"><span class="mark"></span><span class="name">KRTLO</span></div>
  </header>
  <div class="accent-rule"></div>

  <section class="intro">
    The Kertlow Small Business Association (KRTLO) is a local leader in the areas of Arts, Education and Entrepreneurship and is working diligently to promote Kertlow and revitalize our downtown. When you become an KRTLO Member, you will be a part of the citywide work that the KRTLO does every day to improve the lives of citizens of Kertlow.
  </section>

  <div class="goal-tab">What is our goal:</div>
  <section class="goals">
    <div class="goal" style="left:64px;top:67px;width:300px">
      <svg width="20" height="20" viewBox="0 0 20 20"><circle cx="10" cy="10" r="9" fill="var(--green)"/><path d="M5.5 10.2l3 3 6-6.2" stroke="var(--navy)" stroke-width="2.4" fill="none"/></svg>
      <div><b>We promote</b> Kertlow Hotels, Shopping and Events that make Kertlow a pleasant, exciting and prosperous place to live.</div>
    </div>
    <div class="goal small" style="left:401px;top:68px;width:270px">
      <svg width="20" height="20" viewBox="0 0 20 20"><circle cx="10" cy="10" r="9" fill="var(--green)"/><path d="M5.5 10.2l3 3 6-6.2" stroke="var(--navy)" stroke-width="2.4" fill="none"/></svg>
      <div><b>We work</b> with all levels of local gov-ernment to promote our community and create a fertile environment for growth.</div>
    </div>
    <div class="goal" style="left:64px;top:160px;width:300px">
      <svg width="20" height="20" viewBox="0 0 20 20"><circle cx="10" cy="10" r="9" fill="var(--green)"/><path d="M5.5 10.2l3 3 6-6.2" stroke="var(--navy)" stroke-width="2.4" fill="none"/></svg>
      <div><b>We provide</b> training and resources to anyone interested Arts, Education and Entrepreneurship.</div>
    </div>
    <div class="goal" style="left:401px;top:160px;width:280px">
      <svg width="20" height="20" viewBox="0 0 20 20"><circle cx="10" cy="10" r="9" fill="var(--green)"/><path d="M5.5 10.2l3 3 6-6.2" stroke="var(--navy)" stroke-width="2.4" fill="none"/></svg>
      <div><b>We help</b> entrepreneur's start and grow their businesses in a tax efficient and appropriate way.</div>
    </div>
  </section>

  <section class="appeal">
    Every day, we look for ways to help our local businesses grow and expand, but we need you by our side. As an KRTLO Member, you can help provide training, education and support, and you can give our many businesses a chance to grow and our citizens the opportunity to experience big town amenities and events in a small town. Members' regular monthly gifts provide a con-sistent, reliable income stream that allows us to spend less time fundraising—and more time helping our businesses and community. Becoming an KRTLO Member is an easy, efficient and tax-deductible way to make a difference for our community all year long.
    <strong>Please donate today.</strong>
  </section>
</main>
</body>
</html>
```